Flyer für Unterstützung in der Personalarbeit
Zielgruppe
HR Freelancer, bitte Dienstleistung für Unternehmen an, die temporär Unterstützung in der Personalarbeit (Personalprozesse, Recruiting, Lohn- und Gehaltsabrechnung, HR Management, Administration) benötigen.
Aufgabenstellung
Ich benötige einen mehrseitigen Flyer, der mich und meine Arbeit kurz vorstellt. Außerdem soll es in einem Teil darum gehen, warum ein HR Freelancer eine gute Wahl ist. Der Flyer/die Broschüre soll an Unternehmen versendet werden.
Ich wünsche mir ein modernes minimalistisches und dennoch ansprechendes Design. Ich benötige die Datei am Ende auch im Word Format, da ich zukünftig Referenzen und weitere Auftraggeber ergänzen muss.
Ich füge zudem verschiedene Bilder bei, dabei müssen nicht alle berücksichtigt werden.

```html
<!DOCTYPE html>
<html lang="de">
<head>
<meta charset="utf-8">
<title>Lena Hartwig – HR-Freelancerin</title>
<link rel="stylesheet" href="https://fonts.googleapis.com/css2?family=Red+Hat+Display:wght@700;800&family=Inter:wght@400;500;600&display=swap">
<style>
  :root{
    --coral:#e9533f;
    --ink:#2b2b2b;
    --white:#ffffff;
    --rule:rgba(255,255,255,.55);
    --photo-a:#9a948f;
    --photo-b:#5b4a42;
  }
  *{margin:0;padding:0;box-sizing:border-box}
  html,body{width:1200px;height:402px;overflow:hidden;background:var(--white)}
  body{font-family:"Inter",sans-serif;color:var(--ink);position:relative}
  .abs{position:absolute}
  h2,h3,.band,.service-label{font-family:"Red Hat Display",sans-serif;font-weight:800}

  /* Panel 1 */
  .stairs{left:0;top:0;width:21px;height:205px;background:linear-gradient(180deg,#b9b4ae,#8f8a85)}
  .panel-red{left:21px;top:0;width:166px;height:402px;background:var(--coral);color:var(--white)}
  .panel-red h2{position:absolute;left:15px;font-size:15.6px;line-height:1.05}
  .expertise li{position:absolute;left:15px;list-style:none;display:flex;gap:8px;font-size:6.6px;font-weight:600;line-height:1.3;width:150px}
  .expertise svg{flex:0 0 8px;width:8px;height:9px}
  .traits li{position:absolute;left:14px;list-style:none;display:flex;gap:7px;font-size:6.5px;line-height:1.35;width:150px}
  .traits strong{font-weight:600;display:block}
  .traits svg{flex:0 0 9px;width:9px;height:10px}

  /* Panel 2 */
  .portrait{left:188px;top:0;width:214px;height:205px;background:radial-gradient(ellipse at 55% 40%,#b98a6e 0%,var(--photo-b) 45%,var(--photo-a) 100%)}
  .intro{left:224px;top:222px;width:160px}
  .intro h1{font-family:"Red Hat Display",sans-serif;font-weight:800;color:var(--coral);font-size:15.6px;margin-bottom:6px}
  .intro .tagline{font-size:7.8px;font-weight:600;line-height:1.45;margin-bottom:12px}
  .intro p{font-size:6.6px;line-height:1.35;margin-bottom:8px}

  /* Panel 3 */
  .career-title{left:421px;top:17px;font-size:15.6px;color:var(--coral);line-height:1.07}
  .band{position:absolute;background:var(--coral);color:var(--white);font-size:9.3px;line-height:1.05;padding:0 0 0 19px;display:flex;align-items:center}
  .block{position:absolute;font-size:6.6px;line-height:1.33}
  .block h4{color:var(--coral);font-weight:600;font-size:6.6px;margin-bottom:8px}
  .block ul{padding-left:9px}
  .block li{margin-bottom:3.5px}

  /* Panel 4 */
  .panel-services{left:805px;top:0;width:395px;height:402px;background:var(--coral);color:var(--white)}
  .panel-services h2{position:absolute;left:20px;top:17px;font-size:15.6px}
  .service{position:absolute;left:20px;width:363px;display:flex}
  .service-label{width:188px;font-size:9.3px;line-height:1.2}
  .service-text{width:175px;font-size:6.5px;line-height:1.35}
  .rule{position:absolute;left:20px;width:363px;height:0;border-top:.6px solid var(--rule)}
</style>
</head>
<body>

<div class="abs stairs" role="img" aria-label="Foto: helle Steintreppe"></div>

<section class="abs panel-red">
  <h2 style="top:17px">Expertise</h2>
  <ul class="expertise">
    <li style="top:45px"><svg viewBox="0 0 8 9"><rect x=".5" y=".5" width="6" height="7.5" fill="none" stroke="#fff" stroke-width=".9"/><path d="M2 3h3M2 5h2" stroke="#fff" stroke-width=".8"/></svg>HR Generalist / Personalbetreuung</li>
    <li style="top:62px"><svg viewBox="0 0 8 9"><rect x=".5" y=".5" width="6" height="7.5" fill="none" stroke="#fff" stroke-width=".9"/><path d="M2 3h3M2 5h2" stroke="#fff" stroke-width=".8"/></svg>Full Life Cycle Recruiting</li>
    <li style="top:80px"><svg viewBox="0 0 8 9"><rect x=".5" y=".5" width="6" height="7.5" fill="none" stroke="#fff" stroke-width=".9"/><path d="M2 3h3M2 5h2" stroke="#fff" stroke-width=".8"/></svg>Einführung und Betreuung von Bewerbermanagementsystemen</li>
    <li style="top:106px"><svg viewBox="0 0 8 9"><rect x=".5" y=".5" width="6" height="7.5" fill="none" stroke="#fff" stroke-width=".9"/><path d="M2 3h3M2 5h2" stroke="#fff" stroke-width=".8"/></svg>Vorbereitende Lohn- und Gehaltsabrechnung (PERSOLA)</li>
    <li style="top:132px"><svg viewBox="0 0 8 9"><rect x=".5" y=".5" width="6" height="7.5" fill="none" stroke="#fff" stroke-width=".9"/><path d="M2 3h3M2 5h2" stroke="#fff" stroke-width=".8"/></svg>Zusammenarbeit mit Arbeitnehmervertretungen</li>
    <li style="top:159px"><svg viewBox="0 0 8 9"><rect x=".5" y=".5" width="6" height="7.5" fill="none" stroke="#fff" stroke-width=".9"/><path d="M2 3h3M2 5h2" stroke="#fff" stroke-width=".8"/></svg>Berufserfahrung in verschiedenen Dienstleistungsbranchen</li>
    <li style="top:187px"><svg viewBox="0 0 8 9"><rect x=".5" y=".5" width="6" height="7.5" fill="none" stroke="#fff" stroke-width=".9"/><path d="M2 3h3M2 5h2" stroke="#fff" stroke-width=".8"/></svg>Fließende Englischkenntnisse</li>
  </ul>

  <h2 style="top:224px">Was mich<br>auszeichnet</h2>
  <ul class="traits">
    <li style="top:271px"><svg viewBox="0 0 9 10"><circle cx="4.5" cy="4" r="3.5" fill="none" stroke="#fff" stroke-width=".9"/><circle cx="4.5" cy="4" r="1.4" fill="#fff"/><path d="M2.5 7.5 L4.5 9.6 L6.5 7.5" fill="none" stroke="#fff" stroke-width=".9"/></svg><span><strong>Kommunikativ &amp; Organisiert:</strong>Ich setze auf klare Kommunikation und strukturiertes Arbeiten.</span></li>
    <li style="top:306px"><svg viewBox="0 0 9 10"><circle cx="4.5" cy="4" r="3.5" fill="none" stroke="#fff" stroke-width=".9"/><circle cx="4.5" cy="4" r="1.4" fill="#fff"/><path d="M2.5 7.5 L4.5 9.6 L6.5 7.5" fill="none" stroke="#fff" stroke-width=".9"/></svg><span><strong>Empathisch &amp; Diskret:</strong>Der respektvolle Umgang mit Menschen ist mir wichtig.</span></li>
    <li style="top:341px"><svg viewBox="0 0 9 10"><circle cx="4.5" cy="4" r="3.5" fill="none" stroke="#fff" stroke-width=".9"/><circle cx="4.5" cy="4" r="1.4" fill="#fff"/><path d="M2.5 7.5 L4.5 9.6 L6.5 7.5" fill="none" stroke="#fff" stroke-width=".9"/></svg><span><strong>Innovativ &amp; Teamfähig:</strong>Immer offen für neue Ideen und eine starke Teamplayerin.</span></li>
  </ul>
</section>

<div class="abs portrait" role="img" aria-label="Porträtfoto der HR-Freelancerin auf einer Treppe sitzend, mit Smartphone"></div>

<section class="abs intro">
  <h1>Lena Hartwig</h1>
  <p class="tagline">Ihre HR-Freelancerin für<br>maßgeschneiderte Lösungen</p>
  <p>Ich bin eine HR-Generalistin mit über 10 Jahren Erfahrung.</p>
  <p>Als HR-Freelancerin helfe ich Unternehmen dabei, ihre HR-Prozesse zu optimieren und maßgeschneiderte Lösungen zu finden.</p>
  <p>Ob Personalbetreuung, Recruiting oder Prozessverbesserungen – ich kenne die Herausforderungen und packe sie mit Leidenschaft an.</p>
</section>

<h2 class="abs career-title">Berufliche Stationen &amp; relevante<br>Projekterfahrung</h2>

<div class="band" style="left:402px;top:65px;width:195px;height:18px">HR-Freelancerin (seit 2024):</div>
<div class="block" style="left:422px;top:92px;width:172px">
  <h4>Interim HR Operations:</h4>
  <ul>
    <li>Betreuung eines Unternehmens mit ca. 10.000 Mitarbeitenden</li>
    <li>Bearbeitung von HR Operations Anfragen</li>
    <li>Beratung in übergreifenden HR Prozessen zu Disziplinarmaßnahmen, Bescheinigungswesen und Verträgen Administrative und organisatorische Beratung der Teamleitung</li>
    <li>Beratung hinsichtlich der vor- und nachbereitenden Payroll</li>
  </ul>
  <h4 style="margin-top:10px">Senior HR Freelancer:</h4>
  <ul>
    <li>Unterstützung eines Online-Marketing-Unternehmens mit ca. 200 Mitarbeitenden</li>
    <li>Beratung hinsichtlich operativer Personalthemen</li>
    <li>Optimierung des Onboardings und der Personalbetreuung</li>
  </ul>
</div>

<div class="band" style="left:402px;top:289px;width:195px;height:28px">HR-Generalistin bei Norvanta Service<br>Solutions (2018 – 2023):</div>
<div class="block" style="left:421px;top:326px;width:176px">
  <ul>
    <li>Personalbetreuung und -verwaltung von ca. 650 Mitarbeitenden</li>
    <li>Vorbereitung von Lohn- und Gehaltsabrechnungen (PERSOLA)</li>
    <li>Koordination von Personalvorgängen (Einstellungen, Vertragsänderungen, Austritte)</li>
  </ul>
</div>

<div class="block" style="left:612px;top:92px;width:182px">
  <ul>
    <li>Ansprechpartnerin für Mitarbeitende und Führungskräfte</li>
    <li>Durchführung des BEM-Prozesses zur Wiedereingliederung nach Krankheitszeiten</li>
  </ul>
</div>

<div class="band" style="left:605px;top:140px;width:200px;height:28px">Recruitment Manager bei Modavia<br>(2014 – 2018):</div>
<div class="block" style="left:612px;top:177px;width:186px">
  <ul>
    <li>Leitung des deutschlandweiten Recruitment-Teams</li>
    <li>Gesamtverantwortung für den Bewerbungsprozess: Stellenanzeigen, Auswahlgespräche</li>
    <li>Durchführung von High Volume Recruitings bei Neueröffnungen (ca. 300 Mitarbeitende)</li>
    <li>Unterstützung von Führungskräften bei der Rekrutierung und Teamaufbau</li>
  </ul>
</div>

<div class="band" style="left:605px;top:265px;width:200px;height:29px">HR Coordinator bei der KESTRAL<br>Hotelgruppe (2013 – 2014):</div>
<div class="block" style="left:612px;top:303px;width:186px">
  <ul>
    <li>Personaladministration und Bewerbermanagement</li>
    <li>Vorbereitende Lohnabrechnung und Unterstützung des externen Lohnbüros</li>
    <li>Pflege von Personalakten und Stammdaten</li>
    <li>Weiterentwicklung und Implementierung von HR-Prozessen</li>
  </ul>
</div>

<section class="abs panel-services">
  <h2>Leistungen im Überblick</h2>

  <div class="service" style="top:58px"><div class="service-label">Interim HR &amp; Projektmanagement:</div><div class="service-text">Temporäre Übernahme von HR-Aufgaben zur Überbrückung von Vakanzen, Unterstützung in Projekten oder bei Engpässen.</div></div>
  <div class="rule" style="top:93px"></div>
  <div class="service" style="top:101px"><div class="service-label" style="padding-left:3px">Onboarding-Prozesse:</div><div class="service-text">Gestaltung und Optimierung von Onboarding-Prozessen zur schnellen und effektiven Integration neuer Mitarbeiter.</div></div>
  <div class="rule" style="top:136px"></div>
  <div class="service" style="top:143px"><div class="service-label">Recruiting &amp; High Volume<br>Recruiting:</div><div class="service-text">Rekrutierung der passenden Talente für Ihr Unternehmen, inklusive vollständigem Bewerbermanagement und Vorstellungsgesprächen.</div></div>
  <div class="rule" style="top:178px"></div>
  <div class="service" style="top:186px"><div class="service-label">Vorbereitende Abrechnung &amp; Payroll:</div><div class="service-text">Unterstützung bei Lohn- und Gehaltsabrechnungen, einschließlich Pflege von Daten in PERSOLA und Zeiterfassungssystemen.</div></div>
  <div class="rule" style="top:221px"></div>
  <div class="service" style="top:229px"><div class="service-label">Personalbetreuung &amp; Verwaltung:</div><div class="service-text">Umfassende Betreuung Ihrer Mitarbeiter und Sicherstellung reibungsloser Personalprozesse.</div></div>
  <div class="rule" style="top:263px"></div>
  <div class="service" style="top:271px"><div class="service-label">Betriebliches Eingliederungs-<br>management (BEM):</div><div class="service-text">Begleitung und Koordination von BEM-Prozessen zur erfolgreichen Wiedereingliederung nach längeren Krankheitsphasen.</div></div>
  <div class="rule" style="top:305px"></div>
  <div class="service" style="top:314px"><div class="service-label">Zusammenarbeit mit<br>Arbeitnehmervertretungen:</div><div class="service-text">Unterstützung bei der Kommunikation und Verhandlungen mit Betriebsräten zu arbeitsrechtlichen Themen.</div></div>
  <div class="rule" style="top:348px"></div>
  <div class="service" style="top:356px"><div class="service-label">Organisationsentwicklung &amp;<br>Prozessverbesserung:</div><div class="service-text">Analyse und Optimierung von Prozessen zur Steigerung der Effizienz und Flexibilität Ihres Unternehmens.</div></div>
</section>

</body>
</html>
```